Expanding Training Company needs a powerpoint template to deliver a consistent professional image

We want to start with a ppt template that is clean and flexible.
We are a small training organisation focusing on personal effectiveness, leadership, management and change. The MD is a New Zealander living in the United Kingdom and loves the idea of the clean green image that NZ has and wants the PowerPoint template to reflect that. We are pragmatic in what we do - everything comes back to performance improvement. Our clients are big players and our presentations need to be as clean, and as professional as theirs. We need a template that is versatile and can have their logos added as necessary.
Our training tends to be very current and as such we would like to use a lot of images and less words/bullets. We have company colours, logos and fonts that we are happy with and will continue to use.

Here are our company values to give you a sense of what we are about…

As a learning organisation we are always looking to continually improve and renew, our material, ideas, and methods, and are continually on the look out for new techniques, interventions and applications that provide measurable results to our clients.

We think life is about people and relationships, and we are prepared to walk away if people don't keep their word, are untrustworthy or lack integrity, as life is just too short to work with arses.
And because we are not arses we admit when we are wrong and make good on our commitments.

For our clients its all about performance and training is a performance enhancer, we aim to provide training excellence tin all its guises that delivers performance and happy clients.

We harness the value of the team, we believe in Interdependence.

We make life easier for our clients and each other.

Flexibility, innovation and future focus/vision are what our clients can count on us for.

Work is one of many of life's great facilitators, we recognise and value the others - its not just about work.

Industry/Entity Type

It Company

Other font styles liked:
• Avenir Next

Colors
abd037
9bcb3c

Requirements
Must have
• A clean look with multiple options for inserting images, tables, videos, text boxes etc
• copyright information
Nice to have
• Slide masters

```html
<!DOCTYPE html>
<html lang="en">
<head>
<meta charset="utf-8">
<title>Marketing Plan – Slide Template</title>
<link href="https://fonts.googleapis.com/css2?family=Nunito+Sans:wght@400;600;700;800&display=swap" rel="stylesheet">
<style>
  :root{
    --green:#13b24b;
    --lime:#a6c72a;
    --lime-soft:#9bcb3c;
    --ink:#3a3a3a;
    --paper:#ffffff;
    --orange:#f26a21;
    --yellow:#f3d21c;
    --blue:#1e6fc8;
    --chart-yellow:#dcc02a;
    --ring-soft:#a8df95;
  }
  *{box-sizing:border-box;margin:0;padding:0}
  html,body{width:1200px;height:960px;overflow:hidden}
  body{
    background:linear-gradient(180deg,#8f8f8f 0%,#7a7a7a 55%,#565656 100%);
    font-family:"Nunito Sans",Arial,sans-serif;color:var(--ink);
    position:relative;
  }
  .slide{position:absolute;width:390px;height:216px;background:var(--paper);overflow:hidden}
  .slide > svg.art{position:absolute;inset:0;width:100%;height:100%}
  .col-1{left:0}.col-2{left:406px}.col-3{left:810px}
  .row-1{top:14px}.row-2{top:248px}.row-3{top:482px}.row-4{top:714px;height:230px}

  .title{position:absolute;color:var(--green);font-weight:800;font-size:19px;line-height:1;white-space:nowrap}
  .para{position:absolute;font-size:6.4px;line-height:1.32;color:#555;text-align:justify}
  .para p+p{margin-top:6px}
  .tiny{font-size:3.8px;line-height:1.35;color:#9a9a9a}
  .page-no{position:absolute;font-size:4px;color:#777}

  .brand-bar{position:absolute;left:18px;right:0;bottom:6px;display:flex;align-items:flex-end;gap:4px}
  .brand{display:flex;align-items:center;gap:4px;color:var(--green);font-weight:600;font-size:11px;line-height:1;white-space:nowrap}
  .brand .dot{width:12px;height:12px;border-radius:50%;background:var(--green)}
  .rule{flex:1;height:1.5px;background:var(--green);margin-bottom:3px}

  .cover-title{position:absolute;left:18px;top:110px;color:#fff;font-weight:800;font-size:16px}
  .cover-sub{position:absolute;left:18px;top:130px;color:#fff;font-weight:700;font-size:7px}
  .slide-cover .brand-bar{left:286px}

  .icon-grid{position:absolute;left:28px;top:72px;display:grid;grid-template-columns:repeat(3,117px);row-gap:17px}
  .icon-item{display:flex;gap:6px;align-items:center}
  .badge{flex:none;width:18px;height:18px;border-radius:50%;background:var(--lime);display:flex;align-items:center;justify-content:center}
  .badge svg{width:9px;height:9px;fill:#fff}
  .icon-item .tiny{width:82px}

  .photo{position:absolute;left:204px;top:48px;width:166px;height:122px;
    background:linear-gradient(135deg,#e9eef2 0%,#c9d2d8 45%,#8d9aa4 100%)}

  .step-list{position:absolute;left:183px;top:26px}
  .step{height:45px}
  .step b{display:block;font-size:8.5px;color:#333;font-weight:800}
  .step span{display:inline-block;margin-top:8px;border:1px solid var(--orange);border-radius:6px;
    font-size:3.5px;letter-spacing:.5px;padding:1px 6px;color:#555;font-weight:700}

  .feature-row{position:absolute;top:50px;left:26px;right:20px;display:flex;justify-content:space-between}
  .feature{width:102px;text-align:center}
  .feature svg{width:70px;height:70px}
  .feature .tiny{margin-top:10px}
  .placeholder-globe{width:84px;height:70px;margin:0 auto;border-radius:40px;
    background:radial-gradient(circle at 45% 40%,#c9c9c9,#7d7d7d)}

  .list4{position:absolute;left:34px;top:80px;display:grid;grid-template-columns:180px 170px;row-gap:14px}
  .list4 .item{display:flex;gap:5px}
  .list4 .badge{width:12px;height:12px}
  .list4 .badge svg{width:7px;height:7px}
  .list4 h4{font-size:5.4px;color:var(--green);font-weight:700;margin:2px 0 3px}
  .list4 .tiny{width:140px;text-align:justify}

  .projects{position:absolute;left:38px;right:32px;top:48px;display:flex;justify-content:space-between}
  .project{width:78px;text-align:center}
  .project .disc{width:44px;height:44px;border-radius:50%;background:var(--lime-soft);margin:0 auto;display:flex;align-items:center;justify-content:center}
  .project .disc svg{width:15px;height:15px;fill:#fff}
  .project h5{font-size:5.5px;font-weight:700;margin:10px 0 4px;color:#333}
  .project .tiny{color:#666}
  .pill{display:inline-block;margin-top:12px;background:var(--lime-soft);border-radius:6px;
    color:#fff;font-size:3.3px;letter-spacing:.6px;padding:2px 9px;font-weight:700}
  .project:nth-child(even) .pill,.project:nth-child(even) .disc{background:var(--green)}

  .slide-thanks{background:linear-gradient(160deg,#7cbf2a 0%,#2fae3c 45%,#0f9e3e 100%);color:#fff;text-align:center}
  .thanks-head{position:absolute;left:0;right:0;top:96px;font-size:22px;font-weight:600;letter-spacing:.5px}
  .thanks-info{position:absolute;left:0;right:0;top:134px;font-size:5px;line-height:1.35}
  .thanks-info strong{font-size:6.5px;display:block}
  .slide-thanks .brand-bar{left:254px;bottom:14px}
  .slide-thanks .brand{color:#fff}
  .slide-thanks .brand .dot{background:#fff}
  .slide-thanks .rule{background:#fff}
</style>
</head>
<body>

<svg width="0" height="0" style="position:absolute" aria-hidden="true">
  <symbol id="i-lock" viewBox="0 0 10 10"><path d="M3 4V3a2 2 0 014 0v1h1v5H2V4zm1 0h2V3a1 1 0 00-2 0z"/></symbol>
  <symbol id="i-phone" viewBox="0 0 10 10"><path d="M2 1l2 0 1 2-1 1a5 5 0 002 2l1-1 2 1v2c-4 1-8-3-7-7z"/></symbol>
  <symbol id="i-thumb" viewBox="0 0 10 10"><path d="M1 4h2v5H1zM4 4l2-3c1 0 1 1 1 2H9l-1 6H4z"/></symbol>
  <symbol id="i-cart" viewBox="0 0 10 10"><path d="M0 1h2l1 5h5l1-4H3V1zM3 8a1 1 0 102 0 1 1 0 10-2 0zm4 0a1 1 0 102 0 1 1 0 10-2 0z"/></symbol>
  <symbol id="i-pen" viewBox="0 0 10 10"><path d="M1 7l5-5 2 2-5 5H1zM7 1l1-1 2 2-1 1z"/></symbol>
  <symbol id="i-grid" viewBox="0 0 10 10"><path d="M1 1h2v2H1zm3 0h2v2H4zm3 0h2v2H7zM1 4h2v2H1zm3 0h2v2H4zm3 0h2v2H7zM1 7h2v2H1zm3 0h2v2H4zm3 0h2v2H7z"/></symbol>
  <symbol id="i-plus" viewBox="0 0 10 10"><path d="M4 1h2v3h3v2H6v3H4V6H1V4h3z"/></symbol>
  <symbol id="i-clock" viewBox="0 0 10 10"><path d="M5 1a4 4 0 110 8 4 4 0 010-8zm0 1a3 3 0 100 6 3 3 0 000-6zm-.5 1h1v2h1.5v1h-2.5z"/></symbol>
</svg>

<!-- 1: cover -->
<section class="slide slide-cover row-1 col-1">
  <svg class="art" viewBox="0 0 487 270" preserveAspectRatio="none" aria-hidden="true">
    <polygon points="0,0 70,0 205,150 85,270 0,270" fill="var(--green)"/>
    <polygon points="215,160 345,270 80,270" fill="var(--lime)"/>
  </svg>
  <h1 class="cover-title">Marketing Plan</h1>
  <p class="cover-sub">Quarter 1 : 2017</p>
  <div class="brand-bar"><div class="brand"><span class="dot"></span>verdant learning</div><div class="rule"></div></div>
</section>

<!-- 2: text slide -->
<section class="slide row-1 col-2">
  <span class="page-no" style="right:20px;top:16px">2</span>
  <h2 class="title" style="left:30px;top:36px">Title text</h2>
  <div class="para" style="left:144px;top:38px;width:220px">
    <p>Lorem Ipsum is simply dummy text of the printing and typesetting industry. Lorem Ipsum has been the industry's standard dummy text ever since the 1500s, when an unknown printer took a galley of type and scrambled it to make a type specimen book. It has survived not only five centuries, but also the leap into electronic typesetting, remaining essentially unchanged.</p>
    <p>It was popularised in the 1960s with the release of Kernway sheets containing Lorem has survived not only five centuries, but also the leap into electronic typesetting. Lorem Ipsum is simply dummy text of the printing and typesetting industry.</p>
  </div>
  <div class="brand-bar"><div class="brand"><span class="dot"></span>verdant learning</div><div class="rule"></div></div>
</section>

<!-- 3: icon grid -->
<section class="slide row-1 col-3">
  <h2 class="title" style="left:29px;top:22px">Demo Title text</h2>
  <p class="tiny" style="position:absolute;left:30px;top:42px;font-size:5px">Lorem Ipsum is simply</p>
  <div class="icon-grid">
    <div class="icon-item"><span class="badge"><svg><use href="#i-lock"/></svg></span><p class="tiny">Lorem ipsum is simply dummy text of the printing and typesetting industry. Lorem has been.</p></div>
    <div class="icon-item"><span class="badge"><svg><use href="#i-pen"/></svg></span><p class="tiny">Lorem ipsum is simply dummy text of the printing and typesetting industry. Lorem has been.</p></div>
    <div class="icon-item"><span class="badge"><svg><use href="#i-lock"/></svg></span><p class="tiny">Lorem ipsum is simply dummy text of the printing and typesetting industry. Lorem has been.</p></div>
    <div class="icon-item"><span class="badge"><svg><use href="#i-grid"/></svg></span><p class="tiny">Lorem ipsum is simply dummy text of the printing and typesetting industry. Lorem has been.</p></div>
    <div class="icon-item"><span class="badge"><svg><use href="#i-thumb"/></svg></span><p class="tiny">Lorem ipsum is simply dummy text of the printing and typesetting industry. Lorem has been.</p></div>
    <div class="icon-item"><span class="badge"><svg><use href="#i-grid"/></svg></span><p class="tiny">Lorem ipsum is simply dummy text of the printing and typesetting industry. Lorem has been.</p></div>
    <div class="icon-item"><span class="badge"><svg><use href="#i-phone"/></svg></span><p class="tiny">Lorem ipsum is simply dummy text of the printing and typesetting industry. Lorem has been.</p></div>
    <div class="icon-item"><span class="badge"><svg><use href="#i-grid"/></svg></span><p class="tiny">Lorem ipsum is simply dummy text of the printing and typesetting industry. Lorem has been.</p></div>
    <div class="icon-item"><span class="badge"><svg><use href="#i-phone"/></svg></span><p class="tiny">Lorem ipsum is simply dummy text of the printing and typesetting industry. Lorem has been.</p></div>
  </div>
  <span class="page-no" style="right:12px;bottom:16px">3</span>
  <div class="brand-bar"><div class="brand"><span class="dot"></span>verdant learning</div><div class="rule"></div></div>
</section>

<!-- 4: text + photo -->
<section class="slide row-2 col-1">
  <span class="page-no" style="right:20px;top:14px">4</span>
  <h2 class="title" style="left:20px;top:22px">Title text</h2>
  <div class="para" style="left:21px;top:54px;width:150px;font-size:6.8px">
    <p>Lorem Ipsum is simply dummy text of the printing and typesetting industry. Lorem Ipsum has been the industry's standard dummy text ever since the 1500s, when an unknown printer took a galley of type and scrambled it to make a type specimen book.</p>
    <p>It has survived not only five centuries, but also the leap into electronic typesetting, remaining</p>
  </div>
  <div class="photo" role="img" aria-label="Photo of a team gathered around a tablet in a bright office"></div>
  <div class="brand-bar" style="left:2px"><div class="brand"><span class="dot"></span>verdant learning</div><div class="rule"></div></div>
</section>

<!-- 5: step rings -->
<section class="slide row-2 col-2">
  <span class="page-no" style="right:20px;top:14px">7</span>
  <h2 class="title" style="left:30px;top:22px">Title text</h2>
  <div class="para" style="left:33px;top:56px;width:120px;font-size:6.4px">
    <p>Lorem Ipsum is simply dummy text of the printing and typesetting industry. Lorem Ipsum has been the industry's standard dummy text ever since the 1500s, when an unknown printer took a galley of type and scrambled it to make a type specimen book.</p>
    <p>It has survived not only five centuries, but also the leap into electronic.</p>
  </div>
  <div class="step-list">
    <div class="step"><b>+87%</b><span>STEP #1</span></div>
    <div class="step"><b>+68%</b><span>STEP #2</span></div>
    <div class="step"><b>+50%</b><span>STEP #3</span></div>
    <div class="step"><b>+43%</b><span>STEP #4</span></div>
  </div>
  <svg class="art" viewBox="0 0 487 270" preserveAspectRatio="none" role="img" aria-label="Concentric ring chart for 2016">
    <g fill="none" stroke="#e0e0e0" stroke-width=".6">
      <polyline points="270,65 290,65 305,75 320,90"/>
      <polyline points="270,121 290,121 300,115 310,110"/>
      <polyline points="270,177 290,177 300,170 320,160"/>
      <polyline points="270,233 290,233 305,220 320,205"/>
    </g>
    <circle cx="378" cy="136" r="86" fill="none" stroke="var(--ring-soft)" stroke-width="5"/>
    <circle cx="378" cy="136" r="79" fill="none" stroke="#3fb448" stroke-width="7"/>
    <path d="M378 68 A68 68 0 1 1 312 150" fill="none" stroke="var(--orange)" stroke-width="9" stroke-linecap="round"/>
    <circle cx="378" cy="136" r="54" fill="none" stroke="var(--yellow)" stroke-width="8"/>
    <path d="M378 99 A37 37 0 1 1 343 148" fill="none" stroke="var(--blue)" stroke-width="9"/>
    <circle cx="378" cy="136" r="28" fill="#fff"/>
    <circle cx="378" cy="57" r="5" fill="var(--orange)"/>
    <circle cx="378" cy="92" r="4" fill="var(--orange)"/>
    <circle cx="378" cy="186" r="5" fill="var(--blue)"/>
    <circle cx="295" cy="138" r="5" fill="var(--orange)"/>
    <circle cx="397" cy="166" r="4" fill="var(--orange)"/>
    <text x="378" y="140" text-anchor="middle" font-size="11" font-weight="700" fill="#222" font-family="Nunito Sans, Arial, sans-serif">2016</text>
  </svg>
  <div class="brand-bar"><div class="brand"><span class="dot"></span>verdant learning</div><div class="rule"></div></div>
</section>

<!-- 6: three features -->
<section class="slide row-2 col-3">
  <span class="page-no" style="right:18px;top:14px">8</span>
  <h2 class="title" style="left:32px;top:22px">Title text</h2>
  <div class="feature-row">
    <div class="feature">
      <svg viewBox="0 0 70 70" aria-hidden="true"><g fill="none" stroke="#777" stroke-width="9">
        <path d="M20 18A24 24 0 0 1 52 20"/><path d="M58 30A24 24 0 0 1 48 56"/><path d="M36 60A24 24 0 0 1 11 38"/></g>
        <g fill="#777"><polygon points="52,12 60,24 46,25"/><polygon points="52,54 40,62 40,49"/><polygon points="6,34 16,28 18,42"/></g></svg>
      <p class="tiny">Lorem ipsum is simply dummy text of the printing and typesetting industry. Lorem ipsum</p>
    </div>
    <div class="feature">
      <div class="placeholder-globe" role="img" aria-label="Illustration of two globes"></div>
      <p class="tiny">Lorem ipsum is simply dummy text of the printing and typesetting industry. Lorem ipsum</p>
    </div>
    <div class="feature">
      <svg viewBox="0 0 70 70" aria-hidden="true"><g fill="#777">
        <polygon points="35,4 42,14 28,14"/><polygon points="26,17 44,17 49,25 21,25"/><polygon points="19,28 51,28 56,36 14,36"/>
        <rect x="17" y="52" width="4" height="14"/><rect x="24" y="46" width="4" height="20"/><rect x="31" y="40" width="4" height="26"/>
        <rect x="38" y="46" width="4" height="20"/><rect x="45" y="42" width="4" height="24"/><rect x="52" y="50" width="4" height="16"/></g>
        <path d="M36 36v14M29 43h14" stroke="#bbb" stroke-width="4"/></svg>
      <p class="tiny">Lorem ipsum is simply dummy text of the printing and typesetting industry. Lorem ipsum</p>
    </div>
  </div>
  <div class="brand-bar"><div class="brand"><span class="dot"></span>verdant learning</div><div class="rule"></div></div>
</section>

<!-- 7: four items -->
<section class="slide row-3 col-1">
  <h2 class="title" style="left:33px;top:24px">Title text demo</h2>
  <div class="list4">
    <div class="item"><span class="badge"><svg><use href="#i-clock"/></svg></span><div><h4>Demo title text</h4><p class="tiny">Lorem ipsum is simply dummy text of the printing and typesetting industry. Lorem ipsum has been the industry's standard dummy text ever since the 1500s, when an unknown printer took a galley</p></div></div>
    <div class="item"><span class="badge"><svg><use href="#i-clock"/></svg></span><div><h4>Demo title text</h4><p class="tiny">Lorem ipsum is simply dummy text of the printing and typesetting industry. Lorem ipsum has been the industry's standard dummy text ever since the 1500s, when an unknown printer took a galley</p></div></div>
    <div class="item"><span class="badge"><svg><use href="#i-phone"/></svg></span><div><h4>Demo title text</h4><p class="tiny">Lorem ipsum is simply dummy text of the printing and typesetting industry. Lorem ipsum has been the industry's standard dummy text ever since the 1500s, when an unknown printer took a galley</p></div></div>
    <div class="item"><span class="badge"><svg><use href="#i-plus"/></svg></span><div><h4>Demo title text</h4><p class="tiny">Lorem ipsum is simply dummy text of the printing and typesetting industry. Lorem ipsum has been the industry's standard dummy text ever since the 1500s, when an unknown printer took a galley</p></div></div>
  </div>
  <div class="brand-bar" style="left:15px"><div class="brand"><span class="dot"></span>verdant learning</div><div class="rule"></div></div>
</section>

<!-- 8: bar chart -->
<section class="slide row-3 col-2">
  <h2 class="title" style="left:21px;top:20px">Demo Title text</h2>
  <div class="para" style="left:21px;top:58px;width:162px;font-size:6.4px">
    <p>Lorem Ipsum has been the industry's standard dummy text ever since five centuries, but also the leap into electronic typesetting, remaining essentially unchanged. It was popularised in the 1960s with the release of Kernway sheets containing Lorem has survived not only five centuries, but also the leap into electronic typesetting.</p>
  </div>
  <svg class="art" viewBox="0 0 487 270" preserveAspectRatio="none" role="img" aria-label="Stacked bar chart for April to July">
    <g stroke="#ddd" stroke-width=".6" stroke-dasharray="2 2">
      <line x1="303" y1="110" x2="303" y2="198"/><line x1="336" y1="110" x2="336" y2="198"/>
      <line x1="368" y1="110" x2="368" y2="198"/><line x1="400" y1="110" x2="400" y2="198"/><line x1="433" y1="110" x2="433" y2="198"/>
    </g>
    <line x1="271" y1="110" x2="271" y2="198" stroke="#bbb" stroke-width=".6"/>
    <rect x="271" y="114" width="17" height="11" fill="var(--chart-yellow)"/><rect x="288" y="114" width="37" height="11" fill="var(--blue)"/>
    <rect x="271" y="137" width="23" height="11" fill="var(--chart-yellow)"/><rect x="294" y="137" width="29" height="11" fill="var(--blue)"/>
    <rect x="271" y="160" width="40" height="11" fill="var(--chart-yellow)"/><rect x="311" y="160" width="53" height="11" fill="var(--blue)"/>
    <rect x="271" y="183" width="93" height="11" fill="var(--chart-yellow)"/><rect x="364" y="183" width="31" height="11" fill="var(--blue)"/>
    <g font-size="4.5" fill="#666" font-family="Nunito Sans, Arial, sans-serif" text-anchor="end">
      <text x="266" y="121">April</text><text x="266" y="144">May</text><text x="266" y="167">June</text><text x="266" y="190">July</text>
    </g>
    <g font-size="4.5" fill="#666" font-family="Nunito Sans, Arial, sans-serif" text-anchor="middle">
      <text x="271" y="208">0</text><text x="303" y="208">50</text><text x="336" y="208">100</text><text x="368" y="208">150</text><text x="400" y="208">200</text><text x="433" y="208">250</text>
    </g>
  </svg>
  <span class="page-no" style="right:16px;bottom:16px">6</span>
  <div class="brand-bar"><div class="brand"><span class="dot"></span>verdant learning</div><div class="rule"></div></div>
</section>

<!-- 9: projects -->
<section class="slide row-3 col-3">
  <span class="page-no" style="right:14px;top:14px">10</span>
  <h2 class="title" style="left:28px;top:22px">Title text</h2>
  <div class="projects">
    <div class="project"><div class="disc"><svg><use href="#i-lock"/></svg></div><h5>Project Name</h5><p class="tiny">Lorem ipsum is simply dummy text of the printing and typesetting industry. Lorem ipsum but also the</p><span class="pill">NEW PROJECT</span></div>
    <div class="project"><div class="disc"><svg><use href="#i-cart"/></svg></div><h5>Project Name</h5><p class="tiny">Lorem ipsum is simply dummy text of the printing and typesetting industry. Lorem, remaining</p><span class="pill">NEW PROJECT</span></div>
    <div class="project"><div class="disc"><svg><use href="#i-thumb"/></svg></div><h5>Project Name</h5><p class="tiny">Lorem ipsum is simply dummy text of the printing and typesetting industry.</p><span class="pill">NEW PROJECT</span></div>
    <div class="project"><div class="disc"><svg><use href="#i-phone"/></svg></div><h5>Project Name</h5><p class="tiny">Lorem ipsum is simply dummy text of the printing and typesetting industry.</p><span class="pill">NEW PROJECT</span></div>
  </div>
  <div class="brand-bar"><div class="brand"><span class="dot"></span>verdant learning</div><div class="rule"></div></div>
</section>

<!-- 10: thank you -->
<section class="slide slide-thanks row-4 col-2">
  <h2 class="thanks-head">THANK YOU!</h2>
  <p class="thanks-info"><strong>VERDANT LEARNING</strong>48 Fernleaf Lane<br>KT 4410<br>555 0148 22<br>www.verdantlearning.example</p>
  <div class="brand-bar"><div class="brand"><span class="dot"></span>verdant learning</div><div class="rule"></div></div>
</section>

</body>
</html>
```